Greyfield Ridge Medical Website to make connecting and communicating easier

To create a unique, user-friendly, professional website for patients and professionals to access education/ information, forms, appointments, contact details, and data about us, and for us to have the capacity to link to various cloud-based platforms.
To use the logo design and colour scheme we have just sourced.

WEBSITE to be eye catching, Inspiring and alluring
- efficient and logical
- professional and trustworthy appearance
- health focus "living health matters"
- user friendly
- ability to link with cloud-based software and video conferencing tools/ telehealth
- colours- black/ white teal and ?silver

PAGES:
page 1 - Our clinic and staff, services offered, contact us- address/ map / contact details- social media connections
page 2- patients and visitors - New patient forms to complete, news and patient informtion (educatinal)
page 3 - health professionals -referral forms, research and education
page 3- online appointments
page 4 - Quick links - partners, other services
page 5- privacy policy, disclaimer

HI, Could we please extend the deadline another 5 days, so sorry just struggling with my workload to be able to keep up and I am wanting to liaise more with the designer that I will choose. I am so happy with PixelHarbor and all the designers - thank you! Thank you so much!!

Target Market(s)

Patients - mostly over 60's so the website must be minimal clicks and simple to navigate
Professionals - for education and access forms

Industry/Entity Type

Health Care

Coding

Coded - Design and coding required

Number of Pages Required

5+ page

Font styles to use
Sans Serif
Script

Colors
33b8a4
86cfc6

Requirements
Must have
• WEBSITE to be eye catching, Inspiring and alluring
- efficient and logical
- user friendly

WEBSITE - professional and user friendly
- ability to link with cloud based software and videoconferencing/ telehealth
Nice to have
• clean and crisp presentation
happy for an innovative look
room to add more services and ability to link pages and resources
Should not have
• Please ensure the website is not:
clunky
difficult to navigate
common and cheap looking

```html
<!DOCTYPE html>
<html lang="en">
<head>
<meta charset="utf-8">
<title>Greyfield Ridge Medical</title>
<link href="https://fonts.googleapis.com/css2?family=Michroma&family=Roboto:ital,wght@0,400;0,500;0,700;1,400&display=swap" rel="stylesheet">
<style>
:root{
  --teal:#33b8a4;
  --teal-soft:#86cfc6;
  --ink:#111;
  --text:#555;
  --white:#fff;
  --black:#000;
  --hero-a:#0b2c57;
  --hero-b:#2f73b3;
  --map:#e8eaed;
}
*{margin:0;padding:0;box-sizing:border-box}
html,body{width:1200px;height:3513px;overflow:hidden}
body{position:relative;background:var(--white);font-family:'Roboto',sans-serif;color:var(--ink)}
.abs{position:absolute}
.display{font-family:'Michroma',sans-serif;font-weight:400;letter-spacing:1px}
.btn{position:absolute;background:var(--teal);color:var(--white);font:500 16px 'Roboto',sans-serif;display:flex;align-items:center;justify-content:center}

/* header */
.brand{left:89px;top:30px;width:220px;display:flex;align-items:center;gap:8px;color:var(--teal);font:700 17px/1.2 'Roboto',sans-serif}
.brand .mark{width:14px;height:14px;background:var(--teal);flex:none}
.header-book{left:723px;top:15px;width:207px;height:38px}
.header-phone{left:972px;top:24px;color:var(--teal);font:500 16px 'Roboto',sans-serif;display:flex;align-items:center;gap:6px}
.nav{left:332px;top:68px;display:flex;gap:32px;font-size:16px;color:var(--ink)}
.nav .active{color:var(--teal)}

/* hero */
.hero{left:0;top:104px;width:1200px;height:622px;background:linear-gradient(100deg,var(--hero-a),var(--hero-b) 55%,#d9e4ef)}
.hero-title{left:0;top:240px;width:1200px;text-align:center;color:var(--white);font-size:52px}
.hero-sub{left:0;top:310px;width:1200px;text-align:center;color:var(--white);font-size:25px;letter-spacing:4px}
.hero-book{left:496px;top:378px;width:208px;height:40px}
.dots{left:558px;top:613px;display:flex;gap:12px}
.dots span{width:11px;height:11px;border-radius:50%;background:var(--white)}
.dots span.on{background:var(--teal)}

/* about */
.about-title{left:89px;top:818px;font-size:46px}
.about-text{left:89px;top:896px;width:472px;font-size:17px;line-height:38.5px;color:var(--text);text-align:justify}
.read-more{left:89px;top:1204px;width:170px;height:47px;background:var(--teal-soft)}
.about-photo{left:633px;top:799px;width:474px;height:474px;border-radius:50%;background:linear-gradient(135deg,#eef2f6,#c9d3de);border:4px solid var(--teal)}

/* services */
.services-title{left:0;top:1494px;width:1200px;text-align:center;color:var(--white);font-size:46px}
.cards{left:200px;top:1571px;display:flex;gap:12px}
.card{width:192px;height:210px;background:var(--white);border-radius:3px;text-align:center;padding-top:18px}
.card svg{display:block;margin:0 auto}
.card h3{font:400 20px 'Roboto',sans-serif;margin-top:12px;color:var(--ink)}
.card p{font-size:15px;line-height:25px;color:#777;margin-top:8px;padding:0 20px}

/* staff */
.staff-title{left:0;top:2022px;width:1200px;text-align:center;font-size:46px}
.member{top:2107px;width:240px;text-align:center}
.member .photo{width:238px;height:238px;border-radius:50%;border:2px solid var(--teal-soft);padding:8px;margin:0 auto}
.member .photo div{width:100%;height:100%;border-radius:50%;background:linear-gradient(160deg,#7d7f80,#3a3c3d)}
.member h4{font:500 19px 'Roboto',sans-serif;margin-top:22px}
.member p{font:italic 16px 'Roboto',sans-serif;color:#888;margin-top:8px}

/* map / address */
.map{left:0;top:2490px;width:1200px;height:620px;background:var(--map)}
.address{left:160px;top:2615px;width:368px;height:368px;border-radius:50%;background:var(--teal-soft);color:var(--white);text-align:center}
.address h2{font-size:34px;margin-top:74px}
.address p{font-size:16px;line-height:27px}

/* footer */
.footer{left:0;top:3040px;width:1200px;height:473px;background:var(--black)}
.foot-brand{left:89px;top:3205px;width:240px;display:flex;align-items:center;gap:8px;color:var(--teal);font:700 19px 'Roboto',sans-serif}
.foot-brand .mark{width:16px;height:16px;background:var(--teal);flex:none}
.socials{left:109px;top:3312px;display:flex;gap:9px}
.socials span{width:41px;height:41px;border-radius:50%;border:1.5px solid var(--teal);display:flex;align-items:center;justify-content:center}
.col-title{color:var(--teal);font:500 17px 'Roboto',sans-serif;top:3169px}
.links{top:3220px;color:var(--white);font-size:15px;line-height:28.6px;list-style:none}
.news-text{left:781px;top:3220px;width:340px;color:var(--white);font-size:15px;line-height:28.6px}
.email{left:781px;top:3296px;width:329px;height:40px;background:var(--white);color:#888;font-size:14px;padding-left:13px;display:flex;align-items:center}
.subscribe{left:781px;top:3344px;width:329px;height:39px;font-size:17px}
.copy{left:0;top:3478px;width:1200px;text-align:center;color:var(--white);font-size:12px}
</style>
</head>
<body>

<header>
  <div class="abs brand"><span class="mark"></span>Greyfield Ridge Medical</div>
  <a class="btn header-book">Book an Appointments</a>
  <div class="abs header-phone">
    <svg width="14" height="14" viewBox="0 0 24 24"><path fill="#33b8a4" d="M6.6 10.8a15 15 0 0 0 6.6 6.6l2.2-2.2c.3-.3.7-.4 1-.2 1.1.4 2.3.6 3.6.6.6 0 1 .4 1 1V20c0 .6-.4 1-1 1A17 17 0 0 1 3 4c0-.6.4-1 1-1h3.5c.6 0 1 .4 1 1 0 1.3.2 2.5.6 3.6.1.3 0 .7-.2 1z"/></svg>
    + 0 123 456 789
  </div>
  <nav class="abs nav">
    <span class="active">Home</span><span>Patients &amp; Visitors</span><span>Health Professionals</span><span>Online Appointments</span><span>Partners</span><span>Contact Us</span>
  </nav>
</header>

<section>
  <div class="abs hero" role="img" aria-label="Photo of a doctor using a tablet showing medical records"></div>
  <svg class="abs" style="left:0;top:650px" width="1200" height="80" viewBox="0 0 1200 80" preserveAspectRatio="none"><path d="M0 76 Q600 -56 1200 76 L1200 80 L0 80Z" fill="#fff"/></svg>
  <h1 class="abs display hero-title">GREYFIELD RIDGE MEDICAL</h1>
  <p class="abs hero-sub">LIVING HEALTHY MATTERS</p>
  <a class="btn hero-book">Book an Appointments</a>
  <div class="abs dots"><span class="on"></span><span></span><span></span><span></span></div>
</section>

<section>
  <h2 class="abs display about-title">ABOUT US</h2>
  <p class="abs about-text">Lorem ipsum dolor sit amet, consectetur adipiscing elit, sed do eiusmod tempor incididunt ut labore et dolore magna aliqua. Ut enim ad minim veniam, quis nostrud exercitation ullamco laboris nisi ut aliquip ex ea commodo consequat. Duis aute irure dolor in reprehenderit in voluptate velit esse cillum dolore eu fugiat nulla pariatur. Excepteur sint occæcat cupidatat non proident, sunt in culpa qui officia deserunt mollit anim id est laborum.</p>
  <a class="btn read-more">Read More</a>
  <div class="abs about-photo" role="img" aria-label="Photo of hands typing on a laptop showing a medical record"></div>
</section>

<section>
  <svg class="abs" style="left:0;top:1345px" width="1200" height="600" viewBox="0 0 1200 600" preserveAspectRatio="none"><path d="M0 2 Q600 118 1200 2 L1200 596 Q600 480 0 596Z" fill="#86cfc6"/></svg>
  <h2 class="abs display services-title">SERVICES</h2>
  <div class="abs cards">
    <div class="card">
      <svg width="48" height="58" viewBox="0 0 48 58" fill="none" stroke="#33b8a4" stroke-width="1.6"><rect x="6" y="4" width="36" height="50" rx="2"/><path d="M14 16h20M14 26h20M14 34h20M14 42h14"/></svg>
      <h3>Lorem ipsum</h3><p>Lorem ipsum dolor sit amet, consectetur adipiscing elit</p>
    </div>
    <div class="card">
      <svg width="52" height="58" viewBox="0 0 52 58" fill="none" stroke="#33b8a4" stroke-width="1.6"><rect x="6" y="8" width="40" height="42" rx="3"/><path d="M26 8v42M12 20h8M12 28h8M32 20h8M32 28h8M12 36h8"/></svg>
      <h3>Lorem ipsum</h3><p>Lorem ipsum dolor sit amet, consectetur adipiscing elit</p>
    </div>
    <div class="card">
      <svg width="58" height="58" viewBox="0 0 58 58" fill="none" stroke="#33b8a4" stroke-width="1.6"><rect x="8" y="20" width="42" height="34"/><path d="M4 22 29 6l25 16M29 26v12M23 32h12"/></svg>
      <h3>Lorem ipsum</h3><p>Lorem ipsum dolor sit amet, consectetur adipiscing elit</p>
    </div>
    <div class="card">
      <svg width="58" height="58" viewBox="0 0 58 58" fill="none" stroke="#33b8a4" stroke-width="1.6"><rect x="6" y="10" width="34" height="42" rx="2"/><path d="M13 22h20M13 30h20M13 38h14"/><circle cx="48" cy="12" r="5"/></svg>
      <h3>Lorem ipsum</h3><p>Lorem ipsum dolor sit amet, consectetur adipiscing elit</p>
    </div>
  </div>
</section>

<section>
  <h2 class="abs display staff-title">CLINIC AND STAFF</h2>
  <div class="abs member" style="left:89px"><div class="photo"><div role="img" aria-label="Staff portrait photo"></div></div><h4>Lena Marsh</h4><p>Lorem ipsum dolor sit</p></div>
  <div class="abs member" style="left:349px"><div class="photo"><div role="img" aria-label="Staff portrait photo"></div></div><h4>Lena Marsh</h4><p>Lorem ipsum dolor sit</p></div>
  <div class="abs member" style="left:610px"><div class="photo"><div role="img" aria-label="Staff portrait photo"></div></div><h4>Lena Marsh</h4><p>Lorem ipsum dolor sit</p></div>
  <div class="abs member" style="left:870px"><div class="photo"><div role="img" aria-label="Staff portrait photo"></div></div><h4>Lena Marsh</h4><p>Lorem ipsum dolor sit</p></div>
</section>

<section>
  <div class="abs map" role="img" aria-label="Street map showing the clinic location"></div>
  <svg class="abs" style="left:0;top:2488px" width="1200" height="72" viewBox="0 0 1200 72" preserveAspectRatio="none"><path d="M0 0 H1200 V14 Q600 130 0 14Z" fill="#fff"/></svg>
  <svg class="abs" style="left:0;top:3038px" width="1200" height="62" viewBox="0 0 1200 62" preserveAspectRatio="none"><path d="M0 60 Q600 -58 1200 60 V62 H0Z" fill="#000"/></svg>
  <div class="abs address">
    <h2 class="display">ADDRESS</h2>
    <svg style="margin-top:26px" width="12" height="16" viewBox="0 0 12 16"><path fill="#fff" d="M6 0a6 6 0 0 0-6 6c0 4.5 6 10 6 10s6-5.5 6-10a6 6 0 0 0-6-6zm0 8.2A2.2 2.2 0 1 1 6 3.8a2.2 2.2 0 0 1 0 4.4z"/></svg>
    <p style="margin-top:8px">14 Brookside Lane, Ashwell Vale<br>Ashwell, AV3 9QT</p>
    <svg style="margin-top:28px" width="16" height="12" viewBox="0 0 16 12"><path fill="#fff" d="M0 0h16v2L8 7 0 2zm0 4 8 5 8-5v8H0z"/></svg>
    <p style="margin-top:6px">hello@greyfieldridge.example</p>
  </div>
</section>

<footer>
  <div class="abs footer"></div>
  <div class="abs foot-brand"><span class="mark"></span>Greyfield Ridge Medical</div>
  <div class="abs socials"><span></span><span></span><span></span></div>
  <h4 class="abs col-title" style="left:371px">Quick Links</h4>
  <ul class="abs links" style="left:371px"><li>Home</li><li>Patients &amp; Visitors</li><li>Health Professionals</li><li>Online Appointments</li><li>Partners</li><li>Contact Us</li></ul>
  <h4 class="abs col-title" style="left:595px">Others</h4>
  <ul class="abs links" style="left:595px"><li>Privacy policy</li><li>Disclaimer</li></ul>
  <h4 class="abs col-title" style="left:781px">Newsletter</h4>
  <p class="abs news-text">Lorem ipsum dolor sit amet, consectetur adipiscing elit, sed do eiusmod</p>
  <div class="abs email">Enter Your Email Address</div>
  <a class="btn subscribe">Subscribe</a>
  <p class="abs copy">© 2020 The Company Name. All rights Reserved.</p>
</footer>

</body>
</html>
```